Kivo4 Website design (Need help to re-design our website)

We need someone to help us re-design our website and launch it. All contents for the website are ready. (Website: https://www.kivo4.com.au/)

-Rearrange categories:
1. Heat Pumps (Link to PALOX site: https://palox.com.au/)
2. Solar (Under the Solar category; remove solar panels, solar inverters, and solar batteries)
3. LED
4. Capability Statement
5. Service and Support
6. Contact us

Home page - redesign but the free quote will stay.

NOTE:
-Try using professional fonts (Example: Helvetica, etc.)
-Try to play with colours related to sustainability, eco-friendliness, solar, energy, and energy efficiency.
-The website's Footer should be readable and use light colour.

Target Market(s)

Residentials & commercial buildings

Industry/Entity Type

SOLAR ENERGY PROVIDER

Coding

Coded - Design and coding required

Colors

Designer to choose colors to be used in the design.

Requirements
Nice to have
• Effects/transition on the words/copy/images.

```html
<!DOCTYPE html>
<html lang="en">
<head>
<meta charset="utf-8">
<title>Kivo4 – Next Generation Energy Saving Products</title>
<link href="https://fonts.googleapis.com/css2?family=Poppins:wght@400;500;600;700&display=swap" rel="stylesheet">
<style>
:root{
  --green:#3d943a;
  --green-line:#5bae3a;
  --blue:#2b55b0;
  --navy:#1c2c48;
  --ink:#1d1d1d;
  --grey-text:#6b6b6b;
  --band:#f4f4f4;
  --footer:#141414;
  --white:#ffffff;
  --star:#e6bb2e;
}
*{box-sizing:border-box;margin:0;padding:0}
html,body{width:1200px;height:4061px;overflow:hidden}
body{position:relative;background:var(--white);font-family:Helvetica,Arial,sans-serif;color:var(--ink)}
.abs{position:absolute}
.head-font{font-family:'Poppins',Helvetica,sans-serif}

/* header */
.site-header{left:0;top:0;width:1200px;height:66px;background:var(--white)}
.brand{font-family:'Poppins',sans-serif;font-weight:700;color:var(--blue);display:flex;align-items:center;gap:8px}
.brand .dot{width:14px;height:14px;background:var(--green);border-radius:50%}
.site-header .brand{left:32px;top:14px;font-size:28px}
.main-nav{left:282px;top:28px;display:flex;gap:33px;font-family:'Poppins',sans-serif;font-size:12px;font-weight:500;color:var(--ink)}
.contact-tab{left:971px;top:0;width:229px;height:66px}
.contact-tab span{position:absolute;left:74px;top:24px;color:var(--white);font-family:'Poppins',sans-serif;font-size:14px;font-weight:500}

/* hero */
.hero{left:0;top:66px;width:1200px;height:675px;background:linear-gradient(120deg,#0d1a2c 0%,#24344a 45%,#4b4a48 75%,#b57a3a 100%)}
.hero-title{left:63px;top:246px;font-family:'Poppins',sans-serif;font-weight:700;font-size:52px;line-height:64px;color:var(--white)}
.hero-sub{left:63px;top:450px;font-size:20px;color:#5cc44a}
.hero-rule{left:63px;top:492px;width:465px;height:2px;background:var(--green-line)}
.hero-text{left:63px;top:514px;width:480px;font-size:17px;line-height:20.5px;color:var(--white)}

/* quote form */
.quote{left:659px;top:167px;width:486px;height:751px;background:var(--green)}
.quote h2{position:absolute;left:47px;top:46px;font-family:'Poppins',sans-serif;font-size:28px;font-weight:600;color:var(--white)}
.field{position:absolute;left:47px;width:388px;height:54px;background:var(--white);font-size:17px;color:#6d6d6d;padding:18px 0 0 22px}
.q-label{position:absolute;left:52px;font-family:'Poppins',sans-serif;font-size:17px;color:var(--white)}
.check{position:absolute;display:flex;align-items:center;gap:14px;font-size:12px;color:var(--white)}
.check i{width:22px;height:22px;background:var(--white);display:block}
.submit{position:absolute;left:47px;top:672px;width:335px;height:47px;background:var(--blue);color:var(--white);font-family:'Poppins',sans-serif;font-weight:600;font-size:17px;text-align:center;line-height:47px}

/* clients */
.clients{left:55px;top:790px;width:575px;height:80px;display:flex;align-items:center;justify-content:space-between}
.client{font-family:'Poppins',sans-serif;font-weight:700;font-size:16px;color:#c4262e;display:flex;align-items:center;gap:6px}
.client .sq{width:22px;height:22px;background:currentColor}

/* about */
.about-back{left:107px;top:1041px;width:453px;height:265px;background:var(--green-line)}
.about-img{left:61px;top:1057px;width:481px;height:337px;background:linear-gradient(160deg,#3f8fe0 0%,#8fc3f2 40%,#2a4f8a 70%,#1b2f5a 100%)}
.section-title{font-family:'Poppins',sans-serif;font-weight:600;font-size:28px;color:var(--ink)}
.underline{height:2px;background:var(--green-line)}
.about-title{left:618px;top:1073px}
.about-line{left:618px;top:1114px;width:127px}
.about-text{left:618px;top:1142px;width:530px;font-size:17px;line-height:20.5px;color:var(--grey-text)}
.about-text p+p{margin-top:16px}
.btn-blue{background:var(--blue);color:var(--white);font-family:'Poppins',sans-serif;font-weight:600;font-size:17px;text-align:center}
.read-more{left:621px;top:1318px;width:218px;height:46px;line-height:46px}

/* services */
.services{left:0;top:1487px;width:1200px;height:640px;background:var(--band)}
.svc-title{left:0;top:1556px;width:1200px;text-align:center}
.svc-line{left:530px;top:1599px;width:127px}
.svc-card{top:1668px;width:481px;height:379px;background:var(--white)}
.svc-card .ph{height:338px}
.svc-card span{display:block;text-align:center;font-family:'Poppins',sans-serif;font-size:14px;font-weight:500;margin-top:11px}

/* accreditations */
.accred{left:0;top:2127px;width:1200px;height:249px;background:linear-gradient(90deg,#1a2a44 0%,#20314e 60%,#2b4a72 100%)}
.accred-title{left:0;top:2171px;width:1200px;text-align:center;color:var(--white)}
.accred-line{left:540px;top:2214px;width:127px}
.badge{background:#3e7a58}

/* projects */
.proj-title{left:0;top:2466px;width:1200px;text-align:center}
.proj-line{left:533px;top:2510px;width:127px}
.proj{top:2575px;width:317px;height:317px;display:flex;align-items:center;justify-content:center;font-family:'Poppins',sans-serif;font-weight:600;font-size:28px;color:var(--white)}
.arrow{top:2725px;width:31px;height:31px;background:var(--green-line)}

/* reviews */
.rev-brand{left:0;top:2960px;width:1200px;text-align:center;font-family:'Poppins',sans-serif;font-size:46px;font-weight:500;color:var(--blue)}
.rev-brand small{display:block;font-size:11px;color:var(--ink);margin-top:-8px}
.stars{color:var(--star);letter-spacing:2px}
.rev-stars{left:0;top:3062px;width:1200px;text-align:center;font-size:26px}
.review{top:3185px;width:322px;height:261px;border:2px solid #c9c9c9;background:var(--white)}
.review .stars{position:absolute;top:48px;width:100%;text-align:center;font-size:34px}
.review p{position:absolute;top:112px;left:14px;right:14px;text-align:center;font-size:13.5px;line-height:17px;color:var(--grey-text)}
.review .uline{position:absolute;left:110px;top:232px;width:112px;height:2px;background:var(--green-line)}
.avatar{top:3139px;width:80px;height:80px;border-radius:50%}

/* footer */
.footer{left:0;top:3543px;width:1200px;height:467px;background:var(--footer)}
.footer .brand{position:absolute;left:48px;top:92px;font-size:34px;color:#3c6fd0}
.f-contact{left:52px;display:flex;align-items:center;gap:18px;color:var(--white);font-size:17px}
.f-head{font-family:'Poppins',sans-serif;font-weight:600;font-size:20px;color:var(--white)}
.f-link{left:352px;width:114px;font-size:12px;color:#bdbdbd;padding-bottom:6px;border-bottom:2px solid var(--green-line)}
.f-loc{left:557px;display:flex;gap:12px;align-items:flex-start;font-size:11.5px;line-height:14px;color:#bdbdbd}
.f-sign-text{left:862px;top:3690px;width:275px;font-size:13px;line-height:16px;color:#bdbdbd}
.f-input{left:862px;top:3740px;width:250px;height:40px;background:var(--white);font-size:13px;color:#777;text-align:center;line-height:40px}
.f-btn{left:862px;top:3794px;width:250px;height:38px;line-height:38px}
.bottom-bar{left:0;top:4010px;width:1200px;height:51px;background:var(--green-line);color:var(--white);font-size:13px}
.bottom-bar span{position:absolute;top:18px}
</style>
</head>
<body>

<header class="abs site-header">
  <div class="abs brand"><i class="dot"></i>Kivo4</div>
  <nav class="abs main-nav"><span>ABOUT</span><span>HEAT PUMPS</span><span>SOLAR</span><span>LED</span><span>CAPABILITY STATEMENT</span><span>SERVICE &amp; SUPPORT</span></nav>
  <div class="abs contact-tab">
    <svg width="229" height="66" style="position:absolute;left:0;top:0"><polygon points="18,0 229,0 229,66 0,66" fill="#3d943a"/></svg>
    <span>CONTACT US</span>
  </div>
</header>

<section class="abs hero" role="img" aria-label="Solar panels at sunset under a cloudy sky"></section>
<h1 class="abs hero-title">WHY PAY EXCESS<br>FOR YOUR<br>ELECTRICITY?</h1>
<p class="abs hero-sub">Save on electricity costs by switching to solar!</p>
<div class="abs hero-rule"></div>
<p class="abs hero-text">Did you know that you could install a solar system for a lower price than your current&nbsp; electricity costs! If you are paying for electricity, why not pay for greener, cleaner energy?<br>It's that simple.</p>

<form class="abs quote">
  <h2>WANT A FREE QUOTE?</h2>
  <div class="field" style="top:112px">Name</div>
  <div class="field" style="top:191px">Email</div>
  <div class="field" style="top:271px">Phone</div>
  <div class="field" style="top:350px">Address</div>
  <div class="q-label" style="top:430px">I AM INTERESTED IN*</div>
  <div class="check" style="left:52px;top:465px"><i></i>Solar For Home</div>
  <div class="check" style="left:248px;top:465px"><i></i>Solar For Business</div>
  <div class="check" style="left:52px;top:505px"><i></i>Heat Pump For Business</div>
  <div class="check" style="left:248px;top:505px"><i></i>Heat Pump For Home</div>
  <div class="check" style="left:52px;top:543px"><i></i>Others- Solar Batteries, Power Purchase Agreement (PPA)</div>
  <div class="q-label" style="top:583px;left:50px">How Did You Find Us*</div>
  <div class="check" style="left:50px;top:615px;gap:10px"><i></i>Friendlo</div>
  <div class="check" style="left:145px;top:615px;gap:10px"><i></i>Searchly</div>
  <div class="check" style="left:227px;top:615px;gap:10px"><i></i>Viewtube</div>
  <div class="check" style="left:315px;top:615px;gap:10px"><i></i>Referral</div>
  <div class="submit">SUBMIT AND GET A QUOTE</div>
</form>

<div class="abs clients">
  <div class="client" style="color:#1c3f7a"><i class="sq"></i>Courtline Sports</div>
  <div class="client">Meridian Mail</div>
  <div class="client" style="color:#b8141c">Fibrex Labs</div>
  <div class="client" style="color:#1c3f8a">Ironvale Steel</div>
</div>

<div class="abs about-back"></div>
<div class="abs about-img" role="img" aria-label="Rooftop solar panels against a blue sky with sun glare"></div>
<h2 class="abs section-title about-title">ABOUT Kivo4</h2>
<div class="abs underline about-line"></div>
<div class="abs about-text">
  <p>Power bills have risen dramatically in Australia over the past decade, making energy bills amongst the highest utility expense for businesses and households alike.</p>
  <p>We are a completely Australian Owned and Operated company that specialise in adapting the latest technologies to improve your energy efficiency and reduce costs.</p>
</div>
<div class="abs btn-blue read-more">READ MORE</div>

<section class="abs services"></section>
<h2 class="abs section-title svc-title">SERVICES WE PROVIDE</h2>
<div class="abs underline svc-line"></div>
<div class="abs svc-card" style="left:91px">
  <div class="ph" role="img" aria-label="Residential roof covered with solar panels" style="background:linear-gradient(150deg,#8a9aa8,#2c3c55 55%,#9aa0a6)"></div>
  <span>RESIDENTIAL SOLAR</span>
</div>
<div class="abs svc-card" style="left:596px">
  <div class="ph" role="img" aria-label="Aerial view of a commercial shed with rooftop solar in farmland" style="background:linear-gradient(180deg,#7a4e3a,#9a8f86 55%,#6b5a4c)"></div>
  <span>COMMERCIAL SOLAR</span>
</div>

<section class="abs accred" role="img" aria-label="Installer in a hard hat beside solar panels on a dark blue background"></section>
<h2 class="abs section-title accred-title">ACCREDITATIONS &amp; PARTNERS</h2>
<div class="abs underline accred-line"></div>
<div class="abs badge" style="left:84px;top:2282px;width:188px;height:40px;border-radius:20px;background:#3f9a4a"></div>
<div class="abs badge" style="left:333px;top:2275px;width:140px;height:54px;background:#8c2f2f"></div>
<div class="abs badge" style="left:570px;top:2262px;width:84px;height:76px;background:#f2f2f2"></div>
<div class="abs badge" style="left:779px;top:2268px;width:140px;height:66px;background:#f2f2f2"></div>
<div class="abs badge" style="left:1052px;top:2262px;width:53px;height:76px;background:#2a62b8"></div>

<h2 class="abs section-title proj-title">OUR RECENT PROJECTS</h2>
<div class="abs underline proj-line"></div>
<div class="abs arrow" style="left:32px"><svg width="31" height="31"><polyline points="18,9 12,15.5 18,22" fill="none" stroke="#fff" stroke-width="2"/></svg></div>
<div class="abs proj" style="left:99px;background:linear-gradient(180deg,#6f8a6c,#2f4a3a 60%,#4a6648)" role="img" aria-label="Aerial view of a 502 kW ground-mounted solar farm">502 KW</div>
<div class="abs proj" style="left:445px;background:linear-gradient(180deg,#5b86b8,#6c8a5c 45%,#4d6b7a)" role="img" aria-label="Aerial view of a 400 kW solar array">400 KW</div>
<div class="abs proj" style="left:789px;background:linear-gradient(180deg,#7f9aa8,#4f6a58 50%,#3d5a4c)" role="img" aria-label="Aerial view of a 320 kW solar array">320 KW</div>
<div class="abs arrow" style="left:1140px"><svg width="31" height="31"><polyline points="13,9 19,15.5 13,22" fill="none" stroke="#fff" stroke-width="2"/></svg></div>

<div class="abs rev-brand">Revuo<small>Reviews</small></div>
<div class="abs stars rev-stars">★★★★★</div>

<div class="abs review" style="left:71px"><div class="stars">★★★★★</div><p>I had my solar system installed almost a year ago now and I'm super happy with it.The crew that came to do the installation were efficient, courteous and knowledgeable and no question was left unanswered<br>Thankyou Kivo4</p><i class="uline"></i></div>
<div class="abs review" style="left:448px"><div class="stars">★★★★★</div><p>I had my solar system installed almost a year ago now and I'm super happy with it.The crew that came to do the installation were efficient, courteous and knowledgeable and no question was left unanswered<br>Thankyou Kivo4</p><i class="uline"></i></div>
<div class="abs review" style="left:831px"><div class="stars">★★★★★</div><p>I had my solar system installed almost a year ago now and I'm super happy with it.The crew that came to do the installation were efficient, courteous and knowledgeable and no question was left unanswered<br>Thankyou Kivo4</p><i class="uline"></i></div>
<div class="abs avatar" style="left:184px;background:linear-gradient(180deg,#8ea6c4,#2a3c5a)" role="img" aria-label="Solar panels thumbnail"></div>
<div class="abs avatar" style="left:568px;background:linear-gradient(120deg,#1d2a40,#b0602a)" role="img" aria-label="Solar panels at dusk thumbnail"></div>
<div class="abs avatar" style="left:952px;background:linear-gradient(180deg,#d8d8d8,#7a7a7a)" role="img" aria-label="Commercial rooftop panels thumbnail"></div>

<footer class="abs footer">
  <div class="brand"><i class="dot"></i>Kivo4</div>
</footer>
<div class="abs f-contact" style="top:3721px">
  <svg width="22" height="22" viewBox="0 0 24 24"><path d="M6.6 10.8a15 15 0 006.6 6.6l2.2-2.2c.3-.3.7-.4 1-.2 1.1.4 2.3.6 3.6.6.6 0 1 .4 1 1V20c0 .6-.4 1-1 1C10.6 21 3 13.4 3 4c0-.6.4-1 1-1h3.5c.6 0 1 .4 1 1 0 1.3.2 2.5.6 3.6.1.3 0 .7-.2 1z" fill="#5bae3a"/></svg>1300 555 017</div>
<div class="abs f-contact" style="top:3773px">
  <svg width="22" height="18" viewBox="0 0 22 18"><rect x="0" y="2" width="22" height="16" fill="#5bae3a"/><polyline points="0,2 11,10 22,2" fill="none" stroke="#141414" stroke-width="2"/></svg>enquiries@kivo4.com.au</div>

<h3 class="abs f-head" style="left:337px;top:3645px">QUICK LINKS</h3>
<div class="abs f-link" style="top:3710px">HOME</div>
<div class="abs f-link" style="top:3750px">ABOUT US</div>
<div class="abs f-link" style="top:3787px">HEAT PUMP</div>
<div class="abs f-link" style="top:3827px">SOLAR</div>
<div class="abs f-link" style="top:3868px">LED</div>

<h3 class="abs f-head" style="left:557px;top:3641px">LOCATIONS</h3>
<div class="abs f-loc" style="top:3708px"><svg width="18" height="24" viewBox="0 0 18 24"><path d="M9 0a9 9 0 00-9 9c0 6.8 9 15 9 15s9-8.2 9-15a9 9 0 00-9-9z" fill="#5bae3a"/><circle cx="9" cy="9" r="3.5" fill="#141414"/></svg><span>12 Harlow Street Kensley<br>VIC 3031</span></div>
<div class="abs f-loc" style="top:3762px"><svg width="18" height="24" viewBox="0 0 18 24"><path d="M9 0a9 9 0 00-9 9c0 6.8 9 15 9 15s9-8.2 9-15a9 9 0 00-9-9z" fill="#5bae3a"/><circle cx="9" cy="9" r="3.5" fill="#141414"/></svg><span>4B/27 Ardent Drive Norwood<br>QLD 4211</span></div>
<div class="abs f-loc" style="top:3818px"><svg width="18" height="24" viewBox="0 0 18 24"><path d="M9 0a9 9 0 00-9 9c0 6.8 9 15 9 15s9-8.2 9-15a9 9 0 00-9-9z" fill="#5bae3a"/><circle cx="9" cy="9" r="3.5" fill="#141414"/></svg><span>9 Foundry Court Irvale VIC 3498</span></div>
<div class="abs f-loc" style="top:3874px"><svg width="18" height="24" viewBox="0 0 18 24"><path d="M9 0a9 9 0 00-9 9c0 6.8 9 15 9 15s9-8.2 9-15a9 9 0 00-9-9z" fill="#5bae3a"/><circle cx="9" cy="9" r="3.5" fill="#141414"/></svg><span>110/52 Garrison St, Perth WA 6000</span></div>
<div class="abs f-loc" style="top:3924px"><svg width="18" height="24" viewBox="0 0 18 24"><path d="M9 0a9 9 0 00-9 9c0 6.8 9 15 9 15s9-8.2 9-15a9 9 0 00-9-9z" fill="#5bae3a"/><circle cx="9" cy="9" r="3.5" fill="#141414"/></svg><span>21/64 Wharf Street Hobart TAS 7000</span></div>

<h3 class="abs f-head" style="left:861px;top:3641px">SIGNUP FOR UPDATES</h3>
<p class="abs f-sign-text">Get all the latest information on Special Discounts, Products and Offers.</p>
<div class="abs f-input">Email Address</div>
<div class="abs btn-blue f-btn">SIGNUP NOW</div>

<div class="abs bottom-bar">
  <span style="left:50px">© Copyright 2024 Kivo4 All Rights Reserved</span>
  <span style="left:948px">Privacy Policy | CEA Policy</span>
</div>

</body>
</html>
```